Sales Brochure- Generic Line Card 215mm x 140mm

Design a double-sided brochure similar to the attached sample. Cover Page contains a logo and theme that never changes. However, the background picture and the description text on the lower corner will be changed to advertise multiple services. Reverse-side contains Detailed Descriptive text related to the picture on Cover Page as well as Logo and Contact information for the business. Use the Ridgeline Controls website www.ridgelinecontrols.ca for theme, color and contact information. Also, use attached business card design for theme to match. Use the supplied logo. SIZE 215mm x 140mm

Font styles to use
Sans Serif

Colors

Designer to choose colors to be used in the design.

Requirements
Must have
• Look Similar to Sample Brochure but include Ridgeline Controls theme and colors

```html
<!DOCTYPE html>
<html lang="en">
<head>
<meta charset="utf-8">
<title>Line Card Brochure – Inside Spread</title>
<link href="https://fonts.googleapis.com/css2?family=Roboto:wght@400;500;700;900&display=swap" rel="stylesheet">
<style>
  :root{
    --canvas:#ececec;
    --deep-teal:#0d2e30;
    --mid-teal:#164b4d;
    --accent-teal:#1f9a9a;
    --accent-orange:#e4572e;
    --text-light:#e8f0ef;
    --photo-steel:#5b6367;
    --photo-brass:#a9833c;
    --photo-dark:#2a2f31;
  }
  *{box-sizing:border-box;margin:0;padding:0}
  html,body{width:1200px;height:700px;overflow:hidden;background:var(--canvas);font-family:"Roboto",Arial,sans-serif}
  .spread{position:absolute;left:20px;top:161px;width:1160px;height:378px;display:flex}
  .page{position:relative;width:580px;height:378px;overflow:hidden;color:var(--text-light)}
  .page-backdrop{position:absolute;inset:0;background:
      radial-gradient(ellipse at 60% 45%,rgba(40,110,108,.55),transparent 70%),
      linear-gradient(180deg,var(--mid-teal) 0%,var(--deep-teal) 70%,#081d1e 100%)}
  .page--right .page-backdrop{background:
      radial-gradient(ellipse at 40% 50%,rgba(50,130,126,.6),transparent 70%),
      linear-gradient(180deg,#1a5556 0%,var(--deep-teal) 75%,#081d1e 100%)}
  .page--left{box-shadow:inset -14px 0 18px -12px rgba(0,0,0,.55)}
  .page--right{box-shadow:inset 14px 0 18px -12px rgba(0,0,0,.55)}

  .section-title{position:absolute;font-weight:900;font-size:12px;letter-spacing:.2px;color:var(--accent-orange);text-transform:uppercase;text-align:center;transform:translateX(-50%);white-space:nowrap}

  .tile{position:absolute}
  .tile-photo{position:absolute;inset:0;clip-path:polygon(14% 0,100% 0,86% 100%,0 100%)}
  .tile::before,.tile::after{content:"";position:absolute;width:3px;transform:skewX(-12deg)}
  .tile::before{left:-4px;top:35%;bottom:2px;background:var(--accent-teal)}
  .tile::after{right:-4px;top:2px;bottom:35%;background:var(--accent-orange)}
  .tile-caption{position:absolute;top:calc(100% + 3px);right:14px;font-size:7px;font-weight:700;text-transform:uppercase;white-space:nowrap;color:#fff}

  .photo--steel{background:linear-gradient(135deg,#8c9599,var(--photo-steel) 45%,var(--photo-dark))}
  .photo--brass{background:linear-gradient(135deg,#d8b25e,var(--photo-brass) 50%,#4a3a1d)}
  .photo--shop{background:linear-gradient(135deg,#7a6d62,#4a4a48 50%,#1f2324)}
  .photo--robot{background:linear-gradient(135deg,#e3c23a,#6d6a55 45%,#2a2e30)}
  .photo--weld{background:linear-gradient(135deg,#b8c9e0,#4f5f78 40%,#2b2118)}

  .lead{position:absolute;text-align:center;font-size:6.4px;line-height:1.35}
  .lead strong{display:block;color:var(--accent-orange);font-weight:700;font-size:7px}

  .bullets{position:absolute;list-style:none;font-size:6.4px;line-height:1.35}
  .bullets li{position:relative;padding-left:14px;margin-bottom:6px}
  .bullets li::before{content:"›";position:absolute;left:0;top:-2px;color:var(--accent-orange);font-weight:900;font-size:9px}

  .bands{position:absolute;left:0;right:0;top:358px;height:8px}
  .band{position:absolute;top:0;height:8px}
  .band--teal{left:0;width:135px;background:var(--accent-teal)}
  .band--orange{left:143px;right:0;background:var(--accent-orange)}
  .page--right .bands{top:352px}
</style>
</head>
<body>
<main class="spread">
  <section class="page page--left">
    <div class="page-backdrop" role="img" aria-label="Machine shop floor photo in dark teal tones"></div>

    <h2 class="section-title" style="left:310px;top:26px">Computer Numeric Control (CNC)</h2>

    <figure class="tile" style="left:80px;top:50px;width:115px;height:86px">
      <div class="tile-photo photo--steel" role="img" aria-label="Lathe turning a steel part"></div>
      <figcaption class="tile-caption">Lathe / Turning</figcaption>
    </figure>
    <figure class="tile" style="left:200px;top:49px;width:112px;height:86px">
      <div class="tile-photo photo--steel" role="img" aria-label="Milling cutter in a steel block"></div>
      <figcaption class="tile-caption">Milling</figcaption>
    </figure>
    <figure class="tile" style="left:317px;top:48px;width:112px;height:86px">
      <div class="tile-photo photo--steel" role="img" aria-label="Five-axis machining centre"></div>
      <figcaption class="tile-caption">5-Axis</figcaption>
    </figure>
    <figure class="tile" style="left:432px;top:46px;width:112px;height:86px">
      <div class="tile-photo photo--steel" role="img" aria-label="Swiss-type lathe tooling"></div>
      <figcaption class="tile-caption">Swiss</figcaption>
    </figure>

    <p class="lead" style="left:60px;top:152px;width:480px">
      <strong>CNC machining offers the most efficient method of producing steel and plastic components.</strong>
      The CNC is programmed using computer code to generate a digital machining process that can be repeated and precisely controlled. Repetitive tasks such as drilling, threading, and tapping are made simple using this technology.
    </p>

    <h2 class="section-title" style="left:300px;top:218px">Swiss Screw &amp; Small Parts</h2>

    <figure class="tile" style="left:48px;top:252px;width:112px;height:84px">
      <div class="tile-photo photo--steel" role="img" aria-label="Swiss CNC machine cutting a small part"></div>
      <figcaption class="tile-caption">Swiss CNC</figcaption>
    </figure>
    <figure class="tile" style="left:172px;top:250px;width:118px;height:84px">
      <div class="tile-photo photo--brass" role="img" aria-label="Pile of brass screws and small parts"></div>
      <figcaption class="tile-caption">Screws / Small Parts</figcaption>
    </figure>

    <ul class="bullets" style="left:305px;top:262px;width:230px">
      <li>Swiss machining (also known as “screw machining”) is the most effective way to produce small parts like pins, screws, nuts, washers and high volume parts. The Swiss machine utilizes a simultaneous machining method where multiple cutting processes occur at the same time.</li>
      <li>By simultaneously machining different features of a small part the process is dramatically quicker than CNC.</li>
    </ul>

    <div class="bands"><span class="band band--teal"></span><span class="band band--orange"></span></div>
  </section>

  <section class="page page--right">
    <div class="page-backdrop" role="img" aria-label="Automated production line photo in dark teal tones"></div>

    <h2 class="section-title" style="left:288px;top:30px">Automation</h2>

    <figure class="tile" style="left:48px;top:55px;width:108px;height:86px">
      <div class="tile-photo photo--robot" role="img" aria-label="Yellow industrial robot arm"></div>
      <figcaption class="tile-caption">Robotics</figcaption>
    </figure>
    <figure class="tile" style="left:160px;top:55px;width:108px;height:86px">
      <div class="tile-photo photo--steel" role="img" aria-label="Rows of machined production parts"></div>
      <figcaption class="tile-caption">Production</figcaption>
    </figure>

    <ul class="bullets" style="left:292px;top:78px;width:220px">
      <li>Robotics and Automation compliment an advanced manufacturing process by adding to the productivity and efficiency of the system. Not all products benefit from automation when compared to highly skilled machinists.</li>
      <li>However, when properly utilized robotics can add to the competitive advantage of a product line or technology.</li>
    </ul>

    <h2 class="section-title" style="left:292px;top:184px">24HR Service, Repair and Welding</h2>

    <figure class="tile" style="left:58px;top:206px;width:110px;height:82px">
      <div class="tile-photo photo--shop" role="img" aria-label="Machinist at a drill press"></div>
      <figcaption class="tile-caption">24 / 7 Repair</figcaption>
    </figure>
    <figure class="tile" style="left:174px;top:206px;width:110px;height:82px">
      <div class="tile-photo photo--shop" role="img" aria-label="Manual threading lathe"></div>
      <figcaption class="tile-caption">Threading</figcaption>
    </figure>
    <figure class="tile" style="left:290px;top:208px;width:108px;height:82px">
      <div class="tile-photo photo--steel" role="img" aria-label="Zinc phosphate coated steel cylinders"></div>
      <figcaption class="tile-caption">Zinc Phosphate</figcaption>
    </figure>
    <figure class="tile" style="left:406px;top:211px;width:108px;height:82px">
      <div class="tile-photo photo--weld" role="img" aria-label="Welder working on a steel fitting"></div>
      <figcaption class="tile-caption">Welding</figcaption>
    </figure>

    <p class="lead" style="left:80px;top:313px;width:420px">
      <strong>Our 24/7 Service Shop offers conventional and manual machining</strong>
      services for repair and low volume requirements. Conventional machining is performed on manual lathes, mills and drill presses to refurbish tools and other broken equipment.
    </p>

    <div class="bands"><span class="band band--teal"></span><span class="band band--orange"></span></div>
  </section>
</main>
</body>
</html>
```